Form Crafters Business Card

Professional cosmetic surgery company, based in very exclusive area in London. High profiled clientele. Brand is very artistic, modern, state-of-the-art, safe. The best in the business. Celebrity clientele.

Form Crafter’s of London is a brand serving a discriminating and exclusive clientele who value personal service that is both intimate and high end. Our clients choose Form Crafters because of the relationships we share with all of our customers. The clients of Form Crafters have an equal partnership between customers, and very experienced, highly qualified medical professionals. This together provides you with a professional service that keeps you looking good and feeling good. It is a relationship based on honesty, compassion, loyalty and respect.
Form Crafter’s have provided services for internationally recognised celebrities, and other high profiled individuals.

The cards are used for networking at private, exclusive events with VIPs.

Target Market(s)

Professionals
Rich people

Industry/Entity Type

Professional Service

Contact Information for Business Card

Need double sided business card design for 4 people. Back of the business card needs to have contrast background to the front with butterfly watermark with services provided:
Hair Restoration surgery
Hair Loss treatments
Breast surgery
Rhinoplasty
Zelix Liposuction
Fat Grafting
Lumex & Fillers

Front of the business card needs to be a nice satin black.
with following information:
Talvan Desoruthy - name
Chief Executive - Job title

www.formcrafters-example.co.uk
talvan@formcrafters-example.co.uk
Phone: +44 (0)207 146 5327
Mobile: +44 (0)7491 825 436

The London Calder Infirmary
14 Pellmont Street | London | W1K 3TR
Off Dunmore Lane

All business cards have the same address, phone, website as Talvan's details.
Same details on the back of the business card as well.
The other cards have different name, job title, email, mobile number

Kerem Lutz - Name
Partner - Job Title
Former England International Cricketer - please include below job title

email: kerem@formcrafters-example.co.uk
mobile: +44(0)7862 514208

Dr Stellan Vastrel - Name
Plastic Surgeon - Job Title
drvastrel@formcrafters-example.co.uk
No mobile number

Dr Jon Torvick FRCS (please put FRCS in small font) - Name
Hair Restoration Surgeon - Job Title
drtorvick@formcrafters-example.co.uk
No mobile number

Colors
cedeec
85abd2
0655a3

Requirements
Must have
• The logo needs to be in a metallic finish
• Text needs to be striking
• nice background
• butterfly watermark on the back

```html
<!DOCTYPE html>
<html lang="en">
<head>
<meta charset="utf-8">
<title>Form Crafters Business Card</title>
<link rel="stylesheet" href="https://fonts.googleapis.com/css2?family=Marcellus+SC&family=Open+Sans:wght@400&display=swap">
<style>
  :root {
    --page-bg: #e6e6e6;
    --card-light: #a9d8e1;
    --card-dark: #000000;
    --brand-blue: #1a6fc0;
    --text-blue: #2a86d8;
    --accent-orange: #e8741c;
    --divider: #8fb4bd;
  }
  html, body {
    margin: 0;
    padding: 0;
    width: 1200px;
    height: 960px;
    overflow: hidden;
    background: var(--page-bg);
    font-family: "Open Sans", sans-serif;
  }
  .canvas {
    position: relative;
    width: 1200px;
    height: 960px;
  }
  .card {
    position: absolute;
    left: 240px;
    width: 720px;
    height: 420px;
    box-sizing: border-box;
  }
  .card--services { top: 40px; background: var(--card-light); }
  .card--contact { top: 500px; background: var(--card-dark); text-align: center; }

  .mark {
    position: absolute;
    left: 70px;
    top: 150px;
    width: 190px;
    display: flex;
    flex-direction: column;
    align-items: center;
    gap: 14px;
  }
  .mark__dot {
    width: 70px;
    height: 70px;
    border-radius: 50%;
    background: var(--brand-blue);
  }
  .mark__name {
    font-size: 20px;
    color: var(--brand-blue);
  }
  .divider {
    position: absolute;
    left: 320px;
    top: 113px;
    width: 1px;
    height: 208px;
    background: var(--divider);
  }
  .wordmark {
    font-family: "Marcellus SC", serif;
    font-size: 28px;
    color: var(--brand-blue);
    margin: 0;
    letter-spacing: 0.5px;
  }
  .card--services .wordmark {
    position: absolute;
    left: 398px;
    top: 132px;
  }
  .services {
    position: absolute;
    left: 384px;
    top: 185px;
    margin: 0;
    padding: 0;
    list-style: none;
    font-size: 16.5px;
    line-height: 21px;
    color: var(--text-blue);
  }
  .card--contact .wordmark {
    padding-top: 80px;
    color: var(--text-blue);
  }
  .contact {
    margin: 14px 0 0;
    font-size: 16px;
    line-height: 20.5px;
    color: var(--text-blue);
    font-style: normal;
  }
  .address {
    margin: 50px 0 0;
    font-size: 11.5px;
    line-height: 15px;
    color: var(--accent-orange);
    font-style: normal;
  }
</style>
</head>
<body>
<main class="canvas">
  <section class="card card--services" aria-label="Card back with services">
    <div class="mark">
      <span class="mark__dot"></span>
      <span class="mark__name">Form Crafters</span>
    </div>
    <span class="divider"></span>
    <p class="wordmark">Form Crafters</p>
    <ul class="services">
      <li>Hair Restoration surgery</li>
      <li>Hair Loss treatments</li>
      <li>Breast surgery</li>
      <li>Rhinoplasty Zelix Liposuction</li>
      <li>Fat Grafting Lumex &amp; Fillers</li>
    </ul>
  </section>

  <section class="card card--contact" aria-label="Card front with contact details">
    <p class="wordmark">Form Crafters</p>
    <address class="contact">
      Talvan Desoruthy<br>
      Chief Executive<br>
      www.formcrafters-example.co.uk<br>
      talvan@formcrafters-example.co.uk<br>
      Phone: +44 (0)207 146 5327<br>
      Mobile: +44 (0)7491 825 436
    </address>
    <address class="address">
      The London Calder Infirmary<br>
      14 Pellmont Street<br>
      W1K 3TR Off Dunmore Lane<br>
      London
    </address>
  </section>
</main>
</body>
</html>
```